Animal Eye Clinic needs a Business card

We are a new veterinary ophthalmology practice (Tessaly Animal Eye Care) and we need a business card designed. We only see animal eyes - we are not a regular veterinary clinic. We already have a logo. We are looking for a professional, good looking business card to hand out to our clients. We are looking for something simple but professional and contemporary. Our logo is likely the only picture/graphic that needs to be on the card.
Updates

Contact Information for Business Card

Marisol Dunkley, BSc, DVM, MSc, DipACVO
Veterinary Ophthalmologist

Phone: 250.418.3097
Email: tessalyanimaleyecare@mailbrook.net
Website: tessalyanimaleyecare.net
Address: 1840 Pellworth Rd
Kelowna, BC, V4T 8M3

Colors

Designer to choose colors to be used in the design.

Requirements
Must have
• Our logo (attached)

```html
<!DOCTYPE html>
<html lang="en">
<head>
<meta charset="utf-8">
<title>Tessaly Animal Eye Care – Business Card</title>
<link rel="stylesheet" href="https://fonts.googleapis.com/css2?family=Roboto:wght@400;700&family=Open+Sans:wght@400&family=Crimson+Text:wght@400&display=swap">
<style>
  :root {
    --backdrop: #c8c8c8;
    --card: #f3f3f3;
    --card-shade: #e4e4e4;
    --teal: #008b98;
    --teal-dark: #007984;
    --ink: #5e5e5e;
    --ink-soft: #666666;
  }
  * { box-sizing: border-box; margin: 0; padding: 0; }
  html, body {
    width: 1200px; height: 1176px; overflow: hidden;
    background: var(--backdrop);
  }
  .stage { position: relative; width: 1200px; height: 1176px; }

  .card {
    position: absolute; left: 280px; width: 618px; height: 356px;
    border-radius: 22px; overflow: hidden;
    background: linear-gradient(135deg, var(--card-shade) 0%, var(--card) 45%, var(--card-shade) 100%);
  }
  .card--front { top: 190px; }
  .card--back { top: 590px; height: 352px; }

  .brand {
    position: absolute; display: flex; align-items: center; gap: 10px;
  }
  .brand__dot { border-radius: 50%; background: var(--teal); flex: none; }
  .brand__name {
    font-family: "Roboto", Arial, sans-serif; font-weight: 700;
    color: var(--teal); text-transform: uppercase; line-height: 1.1;
  }
  .card--front .brand { top: 34px; right: 34px; }
  .card--front .brand__dot { width: 44px; height: 44px; }
  .card--front .brand__name { font-size: 19px; }

  .person { position: absolute; left: 34px; top: 168px; right: 0; }
  .person__name {
    font-family: "Roboto", Arial, sans-serif; font-weight: 400;
    font-size: 25px; color: var(--ink); letter-spacing: 0.3px;
  }
  .person__creds { font-size: 16px; margin-left: 4px; }
  .person__role {
    display: flex; align-items: center; gap: 4px; margin-top: 1px;
    font-family: "Crimson Text", Georgia, serif; font-size: 16px; color: var(--teal);
  }
  .person__rule { flex: 1; height: 2px; background: var(--teal); }

  .contact {
    position: absolute; top: 244px;
    font-family: "Open Sans", Arial, sans-serif; font-size: 15px; color: var(--ink-soft);
    list-style: none; line-height: 26px;
  }
  .contact--lines { left: 34px; }
  .contact--lines li { display: flex; align-items: center; gap: 10px; }
  .contact--address { right: 34px; text-align: right; }
  .icon { width: 14px; height: 14px; fill: var(--teal); flex: none; }

  .band {
    position: absolute; left: 0; right: 0; bottom: 0; height: 28px;
    background: linear-gradient(90deg, var(--teal-dark), var(--teal));
  }

  .card--back .brand { left: 140px; top: 98px; gap: 24px; }
  .card--back .brand__dot { width: 156px; height: 156px; }
  .card--back .brand__name { font-size: 26px; }
</style>
</head>
<body>
<main class="stage">

  <section class="card card--front" aria-label="Business card front">
    <div class="brand">
      <span class="brand__dot"></span>
      <span class="brand__name">Tessaly<br>Animal Eye Care</span>
    </div>

    <div class="person">
      <h1 class="person__name">MARISOL DUNKLEY,<span class="person__creds">BSC, DVM, MSC, DIPACVO</span></h1>
      <p class="person__role">Veterinary Ophthalmologist <span class="person__rule"></span></p>
    </div>

    <ul class="contact contact--lines">
      <li>
        <svg class="icon" viewBox="0 0 16 16" aria-hidden="true"><path d="M1 6c0-2 3-3 7-3s7 1 7 3v1h-4V5.5H5V7H1zM3 8h10l1 5H2z"/></svg>
        250.418.3097
      </li>
      <li>
        <svg class="icon" viewBox="0 0 16 16" aria-hidden="true"><path d="M1 3h14v10H1z" /><path d="M1 3l7 6 7-6" fill="none" stroke="#f3f3f3" stroke-width="1.4"/></svg>
        tessalyanimaleyecare@mailbrook.net
      </li>
      <li>
        <svg class="icon" viewBox="0 0 16 16" aria-hidden="true"><circle cx="8" cy="8" r="6.5" fill="none" stroke="#008b98" stroke-width="1.3"/><path d="M1.5 8h13M8 1.5c-3 3.5-3 9.5 0 13M8 1.5c3 3.5 3 9.5 0 13" fill="none" stroke="#008b98" stroke-width="1"/></svg>
        tessalyanimaleyecare.net
      </li>
    </ul>

    <ul class="contact contact--address">
      <li>1840 Pellworth Rd</li>
      <li>Kelowna, BC, V4T 8M3</li>
    </ul>

    <div class="band"></div>
  </section>

  <section class="card card--back" aria-label="Business card back">
    <div class="brand">
      <span class="brand__dot"></span>
      <span class="brand__name">Tessaly<br>Animal Eye Care</span>
    </div>
  </section>

</main>
</body>
</html>
```